Alcohol drink bottle label Armenian brandy

I need a complete label for Armenian brandy in russian language АРМЯНСКИЙ КОНЬЯК 5 лет , i have bottles and labe that you can loom on it and make some better copy from it.
Should be in dark yellow and brown colors with armenian motives , symbols
Target Market(s)
Russia
Industry/Entity Type
Brandy Armenian
Font styles to use
Decorative
Colors
FFC000
F8CF3A
FAE287
FDF2CF
FEFAEE
Requirements
Must have
- Russian fonts and Armenian
Nice to have
- The product is in Green frosted bottle round shape

```html
<!DOCTYPE html>
<html lang="ru">
<head>
<meta charset="utf-8">
<title>Армянский коньяк — этикетка</title>
<link rel="stylesheet" href="https://fonts.googleapis.com/css2?family=PT+Serif:wght@700&family=PT+Sans:wght@700&family=Noto+Serif+Armenian:wght@700&display=swap">
<style>
  :root {
    --page-bg: #c2c2c2;
    --gold-deep: #a8731a;
    --gold-mid: #e3b43c;
    --gold-light: #fae287;
    --panel-yellow: #f8cf3a;
    --panel-cream: #fdf2cf;
    --band-red: #a3161a;
    --band-red-dark: #7c0e12;
    --brown: #4a2310;
    --cream-text: #fefaee;
    --scene-tone: #8fa6a0;
  }
  html, body {
    margin: 0;
    width: 1040px;
    height: 1200px;
    overflow: hidden;
    background: var(--page-bg);
  }
  .label {
    display: block;
    width: 1040px;
    height: 1200px;
  }
  .arc-title {
    font-family: "PT Serif", serif;
    font-weight: 700;
    font-size: 38px;
    fill: var(--brown);
    letter-spacing: 1px;
  }
  .arc-armenian {
    font-family: "Noto Serif Armenian", serif;
    font-weight: 700;
    font-size: 18px;
    fill: var(--brown);
    letter-spacing: 3px;
  }
  .brand-name {
    font-family: "PT Serif", serif;
    font-weight: 700;
    font-size: 84px;
    fill: var(--cream-text);
    letter-spacing: 2px;
  }
  .brand-sub {
    font-family: "PT Serif", serif;
    font-weight: 700;
    font-size: 48px;
    fill: var(--gold-light);
    letter-spacing: 2px;
  }
  .spec {
    font-family: "PT Sans", sans-serif;
    font-weight: 700;
    font-size: 22px;
    fill: var(--brown);
  }
  .origin {
    font-family: "PT Sans", sans-serif;
    font-weight: 700;
    font-size: 28px;
    fill: var(--brown);
    letter-spacing: 1px;
  }
</style>
</head>
<body>
<svg class="label" viewBox="0 0 1040 1200" xmlns="http://www.w3.org/2000/svg">
  <defs>
    <linearGradient id="goldFrame" x1="0" y1="0" x2="1" y2="1">
      <stop offset="0" style="stop-color:var(--gold-light)"/>
      <stop offset="0.45" style="stop-color:var(--gold-mid)"/>
      <stop offset="1" style="stop-color:var(--gold-deep)"/>
    </linearGradient>
    <radialGradient id="panelFill" cx="0.5" cy="0.45" r="0.7">
      <stop offset="0" style="stop-color:var(--panel-cream)"/>
      <stop offset="1" style="stop-color:var(--panel-yellow)"/>
    </radialGradient>
    <linearGradient id="bandFill" x1="0" y1="0" x2="0" y2="1">
      <stop offset="0" style="stop-color:var(--band-red)"/>
      <stop offset="1" style="stop-color:var(--band-red-dark)"/>
    </linearGradient>
    <path id="arcPath" d="M250,408 Q520,528 790,408"/>
    <path id="arcArmenianPath" d="M300,452 Q520,548 740,452"/>
  </defs>

  <!-- label frame -->
  <path class="label-frame" fill="url(#goldFrame)"
        d="M65,1065 Q65,1075 75,1075 L965,1075 Q975,1075 975,1065 L975,275 L910,220 Q520,95 130,220 L65,275 Z"/>
  <path class="label-inner-line" fill="var(--band-red)"
        d="M83,1057 L83,283 L142,235 Q520,113 898,235 L957,283 L957,1057 Z"/>
  <path class="label-panel" fill="url(#panelFill)"
        d="M91,1049 L91,287 L148,243 Q520,122 892,243 L949,287 L949,1049 Z"/>

  <!-- landscape vignette -->
  <ellipse cx="520" cy="310" rx="305" ry="142" fill="url(#goldFrame)"/>
  <ellipse class="landscape" cx="520" cy="310" rx="292" ry="130" fill="var(--scene-tone)"
           role="img" aria-label="Illustration of snow-capped Armenian mountains above green hills"/>

  <!-- arched product type ribbon -->
  <path class="title-ribbon" d="M240,380 Q520,500 800,380 L800,428 Q520,548 240,428 Z"
        fill="var(--gold-light)" stroke="var(--gold-deep)" stroke-width="3"/>
  <text class="arc-title"><textPath href="#arcPath" startOffset="50%" text-anchor="middle">АРМЯНСКИЙ КОНЬЯК</textPath></text>
  <text class="arc-armenian" lang="hy"><textPath href="#arcArmenianPath" startOffset="50%" text-anchor="middle">ՀԱՅԿԱԿԱՆ ԿՈՆՅԱԿ</textPath></text>

  <!-- name band -->
  <rect x="91" y="572" width="858" height="6" fill="var(--gold-deep)"/>
  <rect x="91" y="580" width="858" height="180" fill="url(#bandFill)"/>
  <rect x="91" y="762" width="858" height="6" fill="var(--gold-deep)"/>
  <text class="brand-name" x="520" y="668" text-anchor="middle">ДОЛИНСКИЙ</text>
  <text class="brand-sub" x="520" y="732" text-anchor="middle">САД</text>

  <!-- ornaments -->
  <rect class="flourish-left" x="210" y="800" width="170" height="70" rx="35" fill="var(--brown)" opacity="0.75"
        role="img" aria-label="Curled Armenian flourish ornament"/>
  <rect class="emblem" x="445" y="790" width="150" height="195" rx="20" fill="var(--brown)" opacity="0.85"
        role="img" aria-label="Armenian interlaced knot emblem"/>
  <rect class="flourish-right" x="660" y="800" width="170" height="70" rx="35" fill="var(--brown)" opacity="0.75"
        role="img" aria-label="Curled Armenian flourish ornament"/>

  <!-- specifications -->
  <text class="spec" x="225" y="935" text-anchor="middle">ВЫДЕРЖКА</text>
  <text class="spec" x="225" y="962" text-anchor="middle">5 ЛЕТ</text>
  <text class="spec" x="790" y="935" text-anchor="middle">АЛК. 40% ОБ.</text>
  <text class="spec" x="790" y="962" text-anchor="middle">ОБЪЁМ 0,5 Л.</text>

  <text class="origin" x="520" y="1028" text-anchor="middle">ПРОИЗВЕДЕНО В АРМЕНИИ</text>
</svg>
</body>
</html>
```